New business card with our logo

we finalized our logo with the help of pixel harbor - now we need a business card using that logo. we are a metal service center providing raw steel and metal products for fabricating, contractors, artists, etc. we have the wording for the back of the card figured out (attached, no deviations from text please), just need help putting it all together.
would like the look of steel somehow incorporated in the design ... would like the black part of the logo to be steel or silver color (the S & BRANLEY)
Other font styles liked:
- calibri, arial, similar to those, modern looking
Colors
Designer to choose colors to be used in the design.
Requirements
Must have
- Back of card must haves are attached (no deviations from wording please).
- FRONT of card:
- logo
- address
- name
- office tel
- cell
- fax
- website
- address
Nice to have
- incorporate the look of steel or element of steel somehow
- names of the staff on front not in all caps, i.e. Rosvita not ROSVITA
- this industry is more industrial, not coffee or flower shop so design should be aligned with that
- design should be classic and tasteful

```html
<!DOCTYPE html>
<html lang="en">
<head>
<meta charset="utf-8">
<title>Branley Steel Business Card</title>
<link href="https://fonts.googleapis.com/css2?family=Lato:ital,wght@0,400;0,700;1,700&family=Roboto:wght@400;500;700&display=swap" rel="stylesheet">
<style>
  :root {
    --bg: #e9e9eb;
    --blue: #0b72bb;
    --white: #ffffff;
    --steel-dark: #3a3b3d;
    --steel-shadow: #4a4b4d;
  }
  * { margin: 0; padding: 0; box-sizing: border-box; }
  html, body { width: 1200px; height: 849px; overflow: hidden; background: var(--bg); }
  .canvas { position: relative; width: 1200px; height: 849px; }

  .card {
    position: absolute; left: 262px; width: 652px; height: 354px;
    border-radius: 16px; overflow: hidden; background: var(--blue);
    box-shadow: 0 4px 10px rgba(0,0,0,0.18);
  }
  .card-back { top: 46px; color: var(--white); font-family: "Lato", sans-serif; text-align: center; }
  .card-front { top: 446px; font-family: "Roboto", sans-serif; }

  .brand-row { position: absolute; top: 46px; left: 126px; display: flex; align-items: center; gap: 18px; }
  .brand-dot { width: 86px; height: 86px; border-radius: 50%; border: 5px solid var(--white); }
  .brand-name { font-weight: 700; font-size: 40px; letter-spacing: 0.5px; color: var(--white); }

  .back-line { position: absolute; left: 0; right: 0; font-size: 20px; line-height: 1; }
  .service-title { top: 156px; font-size: 24px; font-weight: 700; }
  .services { top: 186px; }
  .products-1 { top: 232px; }
  .products-2 { top: 256px; }
  .tagline { top: 300px; font-weight: 700; font-style: italic; }

  .front-art { position: absolute; inset: 0; }
  .front-brand { position: absolute; left: 44px; top: 138px; display: flex; align-items: center; gap: 14px; }
  .front-dot { width: 84px; height: 84px; border-radius: 50%; border: 6px solid var(--blue); }
  .front-name { font-weight: 700; font-size: 36px; line-height: 1.0; color: var(--steel-dark); }

  .contact { position: absolute; right: 44px; color: var(--white); text-align: right; }
  .person-name { top: 40px; font-size: 26px; font-weight: 700; }
  .person-title { top: 76px; font-size: 15px; }
  .contact-list { top: 156px; font-size: 15px; font-weight: 500; line-height: 20px; right: 30px; }
  .contact-list p { position: relative; }
  .contact-list .gap { margin-top: 18px; }
  .contact-list svg { position: absolute; right: -22px; top: 4px; width: 12px; height: 12px; }
</style>
</head>
<body>
<div class="canvas">

  <section class="card card-back">
    <div class="brand-row">
      <div class="brand-dot"></div>
      <div class="brand-name">BRANLEY STEEL</div>
    </div>
    <p class="back-line service-title">Metal Service Center</p>
    <p class="back-line services">Cut • Shear • Punch • Light Fab</p>
    <p class="back-line products-1">Structural Steel • Stainless &amp; Aluminium</p>
    <p class="back-line products-2">• Building Components • Rebar • Decking......... and more!</p>
    <p class="back-line tagline">Cut to size, Pick-up or Delivered!</p>
  </section>

  <section class="card card-front">
    <svg class="front-art" width="652" height="354" viewBox="0 0 652 354">
      <circle cx="167" cy="178" r="184" fill="var(--steel-shadow)"/>
      <circle cx="153" cy="178" r="184" fill="var(--blue)"/>
      <circle cx="151" cy="178" r="182" fill="var(--white)"/>
    </svg>
    <div class="front-brand">
      <div class="front-dot"></div>
      <div class="front-name">BRANLEY<br>STEEL</div>
    </div>

    <p class="contact person-name">Dorian Velk</p>
    <p class="contact person-title">Managing Director</p>

    <div class="contact contact-list">
      <p>Avenue Corvell 54
        <svg viewBox="0 0 12 12"><path d="M6 1a3.5 3.5 0 0 0-3.5 3.5C2.5 7.5 6 11 6 11s3.5-3.5 3.5-6.5A3.5 3.5 0 0 0 6 1z" fill="none" stroke="#fff" stroke-width="1.3"/><circle cx="6" cy="4.5" r="1.2" fill="#fff"/></svg>
      </p>
      <p>Harlow 1050, Canada</p>
      <p class="gap">+000 000 0000
        <svg viewBox="0 0 12 12"><rect x="3" y="1" width="6" height="10" rx="1" fill="none" stroke="#fff" stroke-width="1.3"/></svg>
      </p>
      <p>+000 000 0000
        <svg viewBox="0 0 12 12"><path d="M9.5 1.5C6 2 3 5 2.5 9.5l2-1 1-2-1-1c.8-1.3 1.8-2.3 3-3l1 1 2-1z" fill="#fff"/></svg>
      </p>
      <p>+000 000 0000
        <svg viewBox="0 0 12 12"><rect x="3" y="1" width="6" height="3" fill="#fff"/><rect x="1" y="4" width="10" height="5" rx="1" fill="#fff"/><rect x="3" y="8" width="6" height="3" fill="#fff"/></svg>
      </p>
      <p>info@branleysteel.com
        <svg viewBox="0 0 12 12"><rect x="1" y="3" width="10" height="7" fill="#fff"/><path d="M1 3l5 4 5-4" fill="none" stroke="var(--blue)" stroke-width="1"/></svg>
      </p>
      <p>www.branleysteel.com
        <svg viewBox="0 0 12 12"><circle cx="6" cy="6" r="5" fill="#fff"/><path d="M1 6h10M6 1c-2 2.5-2 7.5 0 10M6 1c2 2.5 2 7.5 0 10" fill="none" stroke="var(--blue)" stroke-width="0.8"/></svg>
      </p>
    </div>
  </section>

</div>
</body>
</html>
```